Zanquorra Business Card Design

Zanquorra is a small and new restaurant/ bar location in Hong Kong. The name "Djibouti" derives from an African country. There is no specific reason behind other than the fact, that the bar is somewhat inspired by African elements (only inspired but not purely based on African cuisine etc.).

The bar is somewhat a fusion of African, Mediterranean and Oriental (Old French Vietnam) elements.

However, it is very imperative to stress, that the overall look and feel of Zanquorra is a very high end cocktail lounge/ bar location. The bar is tucked away in a hidden alley, so people will have to know about it. The idea is to send the consumer off in an Escape or hidden remote location where they are at ease in a hip, stylish and trendy environment.

The card needs to feel high-end.

Final logo artwork has been attached and also pictures of the bar/ restaurant itself. The logo ie monkey head cannot be modified. However, the background color and the color of the type "ZANQUORRA" can be changed.

The following details need to fit onto the business card. Of course they can be arranged to your liking:

LOGO

Colin Vey
Partner

+852 97035164
xxx@zanquorra.com
www.zanquorra.com
7C, Brennick Road, Wan Chai, Hong Kong

```html
<!DOCTYPE html>
<html lang="en">
<head>
<meta charset="UTF-8">
<title>Zanquorra Business Card</title>
<link rel="stylesheet" href="https://fonts.googleapis.com/css2?family=Open+Sans:wght@400;600;700&display=swap">
<style>
  :root {
    --stage: #8b5e3c;
    --card-light: #ffffff;
    --card-mid: #e6e6e7;
    --card-dark: #cfd0d2;
    --ink: #2a1d17;
    --text-grey: #3a3a3a;
    --band-dark-a: #0a4a86;
    --band-dark-b: #1c78bd;
    --band-light-a: #22a3dc;
    --band-light-b: #0b6db3;
    --white: #ffffff;
    --mark: #2a1d17;
  }
  * { margin: 0; padding: 0; box-sizing: border-box; }
  html, body {
    width: 1200px; height: 521px; overflow: hidden;
    background: var(--stage);
    font-family: "Open Sans", Arial, sans-serif;
  }
  .stage { position: relative; width: 1200px; height: 521px; }

  .card {
    position: absolute;
    width: 464px; height: 265px;
    overflow: hidden;
    box-shadow: 2px 3px 4px rgba(0,0,0,0.35);
  }
  .card-surface {
    position: absolute; inset: 0;
    background:
      linear-gradient(180deg, rgba(255,255,255,0.0) 0%, rgba(255,255,255,0.55) 55%, rgba(255,255,255,0.2) 100%),
      linear-gradient(90deg, var(--card-dark) 0%, var(--card-light) 30%, var(--card-mid) 55%, var(--card-light) 75%, var(--card-dark) 100%);
  }
  .card-front { left: 123px; top: 137px; }
  .card-back  { left: 633px; top: 133px; }

  .brand-disc {
    position: absolute;
    border-radius: 50%;
    background: var(--mark);
    border: 3px solid var(--white);
    box-shadow: 0 0 0 2px var(--mark);
  }
  .card-front .brand-disc { left: 184px; top: 17px; width: 102px; height: 102px; }
  .card-back  .brand-disc { left: 161px; top: 62px; width: 140px; height: 140px; }

  .brand-name {
    position: absolute; left: 0; width: 100%;
    text-align: center;
    font-weight: 700; color: var(--ink);
    letter-spacing: 2px;
  }
  .card-front .brand-name { top: 136px; font-size: 30px; }

  .bands { position: absolute; left: 0; top: 189px; width: 464px; height: 30px; }
  .holder {
    position: absolute; left: 22px; top: 193px;
    color: var(--white); font-size: 17px; font-weight: 600; letter-spacing: 0.5px;
  }
  .holder .role { font-size: 10.5px; letter-spacing: 1.5px; font-weight: 400; }
  .phone {
    position: absolute; right: 24px; top: 193px;
    color: var(--white); font-size: 17px; font-weight: 400; letter-spacing: 0.3px;
  }
  .address {
    position: absolute; left: 21px; top: 224px;
    font-size: 11.5px; line-height: 16px; color: var(--text-grey);
  }
  .contact {
    position: absolute; right: 24px; top: 224px;
    text-align: right; font-size: 11px; line-height: 16px; color: var(--text-grey);
  }
  .contact .label, .contact .web { font-weight: 700; }
  .contact .web { font-size: 11.5px; }

  .card-back .web-line {
    position: absolute; left: 0; width: 100%; top: 210px;
    text-align: center; font-size: 11px; font-weight: 700; color: var(--ink);
  }
  .card-back .brand-name { top: 120px; font-size: 20px; color: var(--white); letter-spacing: 1.5px; }
</style>
</head>
<body>
<main class="stage">

  <section class="card card-front">
    <div class="card-surface"></div>
    <div class="brand-disc"></div>
    <div class="brand-name">ZANQUORRA</div>

    <svg class="bands" viewBox="0 0 464 30" aria-hidden="true">
      <defs>
        <linearGradient id="bandDark" x1="0" x2="1">
          <stop offset="0" stop-color="var(--band-dark-a)"/>
          <stop offset="1" stop-color="var(--band-dark-b)"/>
        </linearGradient>
        <linearGradient id="bandLight" x1="0" x2="1">
          <stop offset="0" stop-color="var(--band-light-a)"/>
          <stop offset="1" stop-color="var(--band-light-b)"/>
        </linearGradient>
      </defs>
      <path d="M0 0 H238 Q232 0 228 8 L220 24 Q217 30 210 30 H0 Z" fill="url(#bandDark)"/>
      <path d="M464 0 H250 Q243 0 240 6 L230 30 H464 Z" fill="url(#bandLight)"/>
    </svg>

    <div class="holder">COLIN VEY, <span class="role">PARTNER</span></div>
    <div class="phone">Tel: +852 97035164</div>

    <div class="address">7C, Brennick Road<br>Wan Chai, Hong Kong</div>
    <div class="contact">
      <span class="label">Email:</span> xxx@zanquorra.com<br>
      <span class="web">www.zanquorra.com</span>
    </div>
  </section>

  <section class="card card-back">
    <div class="card-surface"></div>
    <div class="brand-disc"></div>
    <div class="web-line">www.zanquorra.com</div>
  </section>

</main>
</body>
</html>
```